NEW Modern Sleek Business Card for VR Language Startup

Our startup is using VR to lead the next wave of world language education. We need a two-sided business card that introduces the larger organization (Quorvel Language Inc) and our contact info on one side and shows the product, Lumidrasca, on the other side.

Side 1 (contact info)= Quorvel Logo and Contact info (name, title, phone, email)

Side 2 (product)= Lumidrasc logo, text, and website
Text= Culturally Immersive Language Learning Games
Website= www.lumidrasc.example

Target Market(s)

Education, Technology

Contact Information for Business Card

Contact info will be updated upon approval of the design. For now, put this as a placeholder.

Perry Hollins
Founder & CEO
phollins@mailtrove.example
(555)-014-2736

Font styles to use
Other font styles liked:
• Gibson and Century Gothic are the brand fonts

Requirements
Nice to have
• I would love to see cohesion between the design and colors of the two logos. I have attached a few business card designs that I like, so you can get a feel for my preferred style.

```html
<!DOCTYPE html>
<html lang="en">
<head>
<meta charset="utf-8">
<title>Quorvel Language — Business Card</title>
<link rel="stylesheet" href="https://fonts.googleapis.com/css2?family=Questrial&family=Jost:wght@400;500;600&family=Montserrat:wght@600&display=swap">
<style>
  :root {
    --backdrop: #d9d9d9;
    --card-dark: #0d0d0d;
    --card-mid: #232323;
    --brand-blue: #4f86f5;
    --brand-violet: #6a55f2;
    --text-white: #ffffff;
    --text-grey: #5a5a5a;
    --accent-orange: #ff6a3d;
    --accent-red: #f2304f;
    --accent-purple: #8a4fe0;
    --accent-cyan: #19e3ec;
    --icon-red: #e8323a;
  }
  * { box-sizing: border-box; margin: 0; padding: 0; }
  html, body { width: 1200px; height: 1200px; overflow: hidden; }
  body { background: var(--backdrop); position: relative; }

  .card {
    position: absolute;
    top: 256px;
    width: 396px;
    height: 685px;
    border-radius: 26px;
    overflow: hidden;
    box-shadow: 0 6px 18px rgba(0,0,0,0.35);
  }

  /* Product side */
  .card--product {
    left: 154px;
    background: linear-gradient(100deg, var(--card-dark), var(--card-mid));
    font-family: "Questrial", sans-serif;
    text-align: center;
  }
  .product-mark {
    position: absolute;
    left: 50%; top: 222px;
    width: 110px; height: 110px;
    margin-left: -55px;
    border-radius: 50%;
    background: var(--brand-blue);
  }
  .product-name {
    position: absolute;
    left: 0; right: 0; top: 352px;
    font-size: 50px;
    line-height: 1;
    color: var(--brand-blue);
  }
  .product-tagline {
    position: absolute;
    left: 0; right: 0; top: 410px;
    font-size: 15.5px;
    line-height: 20px;
    color: var(--brand-violet);
  }
  .product-website {
    position: absolute;
    left: 0; right: 0; top: 619px;
    font-size: 15px;
    font-weight: bold;
    color: var(--text-grey);
    letter-spacing: 0.3px;
  }

  /* Contact side */
  .card--contact {
    left: 654px;
    background: linear-gradient(90deg, var(--card-dark), var(--card-mid));
    text-align: center;
    color: var(--text-white);
  }
  .company-mark {
    position: absolute;
    left: 50%; top: 42px;
    width: 100px; height: 100px;
    margin-left: -50px;
    border-radius: 50%;
    background: var(--accent-red);
  }
  .company-name {
    position: absolute;
    left: 0; right: 0; top: 160px;
    font-family: "Montserrat", sans-serif;
    font-weight: 600;
    font-size: 32px;
    line-height: 44px;
    letter-spacing: 9px;
    padding-left: 9px;
    text-transform: uppercase;
    color: var(--text-white);
  }
  .person-name {
    position: absolute;
    left: 0; right: 0; top: 385px;
    font-family: "Jost", sans-serif;
    font-weight: 600;
    font-size: 25px;
  }
  .person-title {
    position: absolute;
    left: 0; right: 0; top: 420px;
    font-family: "Jost", sans-serif;
    font-size: 15px;
  }
  .contact-list {
    position: absolute;
    left: 0; right: 0; top: 560px;
    list-style: none;
    font-family: "Jost", sans-serif;
    font-size: 15px;
  }
  .contact-item {
    display: flex;
    justify-content: center;
    align-items: center;
    gap: 5px;
    height: 30px;
  }
  .contact-icon { width: 13px; height: 13px; fill: var(--icon-red); }

  .color-bar {
    position: absolute;
    left: 0; right: 0; bottom: 0;
    height: 8px;
    display: flex;
    gap: 2px;
    padding: 0 12px;
  }
  .color-bar span { display: block; height: 100%; }
  .bar-orange { background: var(--accent-orange); width: 76px; }
  .bar-red { background: var(--accent-red); width: 106px; }
  .bar-purple { background: var(--accent-purple); width: 106px; }
  .bar-cyan { background: var(--accent-cyan); flex: 1; }
</style>
</head>
<body>

<section class="card card--product" aria-label="Product side">
  <div class="product-mark"></div>
  <h1 class="product-name">Lumidrasc</h1>
  <p class="product-tagline">Culturally Immersive Language<br>Learning Games</p>
  <p class="product-website">www.lumidrasc.example</p>
</section>

<section class="card card--contact" aria-label="Contact side">
  <div class="company-mark"></div>
  <h2 class="company-name">Quorvel<br>Language</h2>
  <p class="person-name">PERRY HOLLINS</p>
  <p class="person-title">President</p>
  <ul class="contact-list">
    <li class="contact-item">
      <svg class="contact-icon" viewBox="0 0 24 24" aria-hidden="true"><path d="M6.6 10.8a15.1 15.1 0 0 0 6.6 6.6l2.2-2.2a1 1 0 0 1 1-.25 11.4 11.4 0 0 0 3.6.57 1 1 0 0 1 1 1V20a1 1 0 0 1-1 1A17 17 0 0 1 3 4a1 1 0 0 1 1-1h3.5a1 1 0 0 1 1 1c0 1.25.2 2.45.57 3.57a1 1 0 0 1-.25 1z"/></svg>
      <span>(555)-014-2736</span>
    </li>
    <li class="contact-item">
      <svg class="contact-icon" viewBox="0 0 24 24" aria-hidden="true"><path d="M2 5h20v14H2z M4 7v.4l8 5.2 8-5.2V7z" fill-rule="evenodd"/></svg>
      <span>phollins@mailtrove.example</span>
    </li>
  </ul>
  <div class="color-bar">
    <span class="bar-orange"></span><span class="bar-red"></span><span class="bar-purple"></span><span class="bar-cyan"></span>
  </div>
</section>

</body>
</html>
```